Create New Bussiness Card For New Shoes Store

Vandrel is a store that sells a variety of skateboard shoes such as Kolvo, Frisk etc. we also sell some skateboard and all skateboard accessories.
we like black and white style logo, but also like blue as well.
We are fully assembled with a deck, truck, wheels, and bearings. Add some personality to your board with a fun, graphic skateboard deck. Constructed of thick 7 ply maple,
Target Market(s)
Target audience: 12-40 year old
especially for young man
Industry/Entity Type
Industrial
Contact Information for Business Card
Name: Vandrel
Address1: 2493 Marlow Pike Rd
City: Xenia
State: Ohio
Zip: 45385
Country: US
Phone: 614583062
email: danbrellick@quortmail.example

```html
<!DOCTYPE html>
<html lang="en">
<head>
<meta charset="utf-8">
<title>Vandrel Business Card</title>
<link rel="stylesheet" href="https://fonts.googleapis.com/css2?family=Josefin+Sans:wght@300&family=Arimo:wght@400&display=swap">
<style>
  :root {
    --orchid: #b466b3;
    --charcoal: #545454;
    --paper: #ffffff;
    --backdrop: #ecebe8;
    --ink-light: #f4f4f4;
  }
  * { margin: 0; padding: 0; box-sizing: border-box; }
  html, body {
    width: 1200px; height: 950px; overflow: hidden;
    background: var(--backdrop);
  }
  .sheet {
    width: 1200px; height: 950px;
    display: flex; flex-direction: column;
    align-items: center; justify-content: center; gap: 34px;
  }
  .card {
    position: relative;
    width: 760px; height: 434px;
    overflow: hidden;
    box-shadow: 0 8px 22px rgba(0,0,0,0.18);
  }
  .card--back { background: var(--orchid); }
  .card--front { background: var(--paper); }

  .wordmark {
    display: flex; align-items: center; gap: 16px;
    font-family: "Josefin Sans", sans-serif; font-weight: 300;
    font-size: 74px; letter-spacing: 1px; line-height: 1;
    white-space: nowrap;
  }
  .wordmark__dot {
    width: 26px; height: 26px; border-radius: 50%;
    border: 3px solid currentColor;
  }
  .card--back .wordmark {
    position: absolute; left: 50%; top: 150px; transform: translateX(-50%);
    color: var(--paper);
  }
  .card--back .site {
    position: absolute; left: 0; right: 0; top: 322px; text-align: center;
    font-family: "Arimo", sans-serif; font-size: 17px; letter-spacing: 3px;
    color: var(--paper);
  }
  .card--front .wordmark {
    position: absolute; left: 68px; top: 180px;
    color: var(--orchid);
  }
  .panel { position: absolute; inset: 0; }
  .contact {
    position: absolute; right: 38px; top: 120px;
    text-align: right;
    font-family: "Arimo", sans-serif; color: var(--ink-light);
  }
  .contact__name {
    font-size: 26px; color: var(--orchid); margin-bottom: 22px;
  }
  .contact__line {
    display: flex; justify-content: flex-end; align-items: center; gap: 8px;
    font-size: 19px; line-height: 30px; white-space: nowrap;
  }
  .contact__line svg { width: 18px; height: 18px; flex: none; }
</style>
</head>
<body>
<main class="sheet">
  <section class="card card--back">
    <div class="wordmark"><span class="wordmark__dot"></span><span>Vandrel</span></div>
    <p class="site">www.vandrel.example</p>
  </section>

  <section class="card card--front">
    <div class="wordmark"><span class="wordmark__dot"></span><span>Vandrel</span></div>
    <svg class="panel" width="760" height="434" viewBox="0 0 760 434" aria-hidden="true">
      <circle cx="820" cy="230" r="352" fill="none" stroke="var(--orchid)" stroke-width="6"/>
      <circle cx="822" cy="230" r="340" fill="var(--charcoal)"/>
    </svg>
    <div class="contact">
      <p class="contact__name">Nate Corwin</p>
      <p class="contact__line">2493 Marlow Pike Rd</p>
      <p class="contact__line">Brackton, Iowa 50321, US</p>
      <p class="contact__line">614583062
        <svg viewBox="0 0 20 20"><path d="M5 2h3l1.5 4-2 1.5a10 10 0 0 0 5 5l1.5-2 4 1.5v3a2 2 0 0 1-2 2A15 15 0 0 1 3 4a2 2 0 0 1 2-2z" fill="var(--orchid)"/></svg>
      </p>
      <p class="contact__line">nate@vandrel.example
        <svg viewBox="0 0 20 20"><rect x="2" y="4" width="16" height="12" rx="1.5" fill="var(--orchid)"/><path d="M2.5 5l7.5 6 7.5-6" fill="none" stroke="var(--charcoal)" stroke-width="1.5"/></svg>
      </p>
      <p class="contact__line">www.vandrel.example
        <svg viewBox="0 0 20 20"><circle cx="10" cy="10" r="8" fill="var(--orchid)"/><path d="M2 10h16M10 2c-3 3-3 13 0 16M10 2c3 3 3 13 0 16" fill="none" stroke="var(--charcoal)" stroke-width="1.2"/></svg>
      </p>
    </div>
  </section>
</main>
</body>
</html>
```